Business Card Redesign

We would like to redesign our existing business cards.
The new design shall look:
ELEGANT, LUXURY, PROFESSIONAL
Reference:
YOU CAN VISIT WWW.LUMEN-BRIDGE-PARTNERS.EXAMPLE FOR BETTER UNDERSTANDING OF COMPANY STRATEGY AND POSITION
Additional:
CHOSEN CANDIDATE SHALL PROVIDE THE INSTRUCTION OF PRINTING IF ANY THERMAL COVERAGE OR ANY ADDITION IS OFFERED
Industry/Entity Type
Business

```html
<!DOCTYPE html>
<html lang="en">
<head>
<meta charset="utf-8">
<title>Lumen Bridge Partners – Business Card</title>
<link rel="stylesheet" href="https://fonts.googleapis.com/css2?family=EB+Garamond:wght@400&family=Open+Sans:wght@400;600&display=swap">
<style>
  :root {
    --backdrop: #4a3426;
    --card-light: #ffffff;
    --card-shade: #e4e4e6;
    --gold: #e9b034;
    --navy: #1b5c9e;
    --ink-blue: #1f5fa3;
    --ink-grey: #6b6b6b;
  }
  * { margin: 0; padding: 0; box-sizing: border-box; }
  html, body {
    width: 1200px;
    height: 900px;
    overflow: hidden;
    background: var(--backdrop);
  }
  .canvas {
    position: relative;
    width: 1200px;
    height: 900px;
  }
  .card {
    position: absolute;
    left: 100px;
    top: 165px;
    width: 1000px;
    height: 570px;
    overflow: hidden;
    background: radial-gradient(ellipse at 55% 45%, var(--card-light) 0%, var(--card-light) 25%, var(--card-shade) 100%);
    font-family: "Open Sans", Arial, sans-serif;
    color: var(--ink-blue);
  }
  .card-shapes {
    position: absolute;
    inset: 0;
  }
  .brand-mark {
    position: absolute;
    left: 80px;
    top: 140px;
    display: flex;
    align-items: center;
    gap: 14px;
  }
  .brand-dot {
    width: 56px;
    height: 56px;
    border-radius: 50%;
    background: var(--navy);
    flex: none;
  }
  .brand-name {
    font-family: "Open Sans", Arial, sans-serif;
    font-weight: 600;
    font-size: 20px;
    line-height: 1.2;
    color: var(--navy);
    width: 150px;
  }
  .company-name {
    position: absolute;
    right: 175px;
    top: 70px;
    font-family: "EB Garamond", Georgia, serif;
    font-size: 38px;
    font-weight: 400;
    color: var(--ink-blue);
  }
  .person {
    position: absolute;
    right: 175px;
    top: 145px;
    text-align: right;
  }
  .person-name {
    font-size: 38px;
    font-weight: 400;
    line-height: 1.1;
    color: var(--ink-blue);
  }
  .person-role {
    font-size: 17px;
    color: var(--ink-grey);
  }
  .phone-lines {
    position: absolute;
    right: 420px;
    top: 425px;
    text-align: right;
    font-size: 19px;
    line-height: 1.35;
  }
  .divider {
    position: absolute;
    left: 596px;
    top: 375px;
    width: 3px;
    height: 140px;
    background: var(--gold);
  }
  .address {
    position: absolute;
    left: 615px;
    top: 370px;
    font-size: 17px;
    line-height: 1.4;
  }
  .website {
    font-size: 21px;
    margin-top: 2px;
  }
</style>
</head>
<body>
<main class="canvas">
  <article class="card">
    <svg class="card-shapes" width="1000" height="570" viewBox="0 0 1000 570" aria-hidden="true">
      <path class="gold-sweep" d="M0,0 L85,0 C20,170 90,440 430,570 L0,570 Z" fill="var(--gold)"/>
      <path class="navy-band" d="M810,0 L1000,0 L1000,500 C975,320 925,140 810,0 Z" fill="var(--navy)"/>
    </svg>

    <div class="brand-mark">
      <span class="brand-dot"></span>
      <span class="brand-name">Lumen Bridge Partners</span>
    </div>

    <h1 class="company-name">Lumen Bridge Partners Limited</h1>

    <div class="person">
      <p class="person-name">Nadia Orlen</p>
      <p class="person-role">PR Consultant</p>
    </div>

    <div class="phone-lines">
      <p>Tel : (852) 2000-4182</p>
      <p>Fax: (852) 2000-4187</p>
    </div>

    <span class="divider"></span>

    <address class="address" style="font-style: normal;">
      <p>Headquarters (Hong Kong)</p>
      <p>Rm. 1204B, 12/F, Harbourline Tower,</p>
      <p>48 Example Road, Central,</p>
      <p>Hong Kong</p>
      <p class="website">www.lumen-bridge-partners.example</p>
    </address>
  </article>
</main>
</body>
</html>
```